Talvex Industrial Maintenance Business Card

Design a business card with the following information, logo must be included.
Talvex Industrial Maintenance
Dale Virnow Jr.
Pone 413-627-8154
email dale.virnow.jr@brindlemail.net

```html
<!DOCTYPE html>
<html lang="en">
<head>
<meta charset="UTF-8">
<title>Talvex Industrial Maintenance — Business Card</title>
<link rel="stylesheet" href="https://fonts.googleapis.com/css2?family=Montserrat:wght@400;500;700&display=swap">
<style>
  :root {
    --brand-blue: #0b6fc4;
    --brand-blue-deep: #0a5fae;
    --brand-blue-light: #1f86dc;
    --ink-grey: #555a60;
    --rule-grey: #b9bdc2;
    --paper: #ffffff;
    --backdrop: #d9dbde;
  }
  * { box-sizing: border-box; margin: 0; padding: 0; }
  html, body {
    width: 1200px; height: 800px; overflow: hidden;
    background: var(--backdrop);
    font-family: "Montserrat", Arial, sans-serif;
  }
  .canvas { position: relative; width: 1200px; height: 800px; }

  .card {
    position: absolute;
    width: 520px; height: 297px;
    box-shadow: 0 10px 24px rgba(0,0,0,0.18);
  }
  .card--front {
    left: 60px; top: 130px;
    background: var(--paper);
    border-bottom: 3px solid var(--brand-blue);
    display: flex; flex-direction: column; align-items: center; justify-content: center;
  }
  .card--back {
    left: 620px; top: 373px;
    background: var(--brand-blue);
    overflow: hidden;
  }

  .brand {
    display: flex; align-items: center; gap: 12px;
    color: var(--brand-blue);
    font-weight: 700;
  }
  .brand__dot {
    width: 46px; height: 46px; border-radius: 50%;
    background: var(--brand-blue);
    flex: none;
  }
  .brand__name { line-height: 1; text-transform: uppercase; }
  .brand__main { display: block; font-size: 44px; letter-spacing: 1px; }
  .brand__sub { display: block; font-size: 11.5px; letter-spacing: 0.6px; margin-top: 4px; }

  .contact { margin-top: 30px; text-align: center; }
  .contact__name {
    color: var(--brand-blue); font-weight: 700; font-size: 21px;
    text-transform: uppercase; letter-spacing: 0.5px;
  }
  .contact__rule {
    width: 210px; height: 1px; background: var(--rule-grey);
    margin: 9px auto 10px;
  }
  .contact__line {
    color: var(--ink-grey); font-weight: 500; font-size: 15px;
    text-transform: uppercase; letter-spacing: 0.6px; line-height: 1.45;
  }

  .back-texture {
    position: absolute; inset: 0;
    background: linear-gradient(135deg, var(--brand-blue-deep) 0%, var(--brand-blue) 50%, var(--brand-blue-light) 100%);
  }
  .brand--reverse {
    position: absolute; right: 40px; bottom: 58px;
    color: var(--paper);
  }
  .brand--reverse .brand__dot { background: var(--paper); width: 38px; height: 38px; }
  .brand--reverse .brand__main { font-size: 36px; }
  .brand--reverse .brand__sub { font-size: 9.5px; }
</style>
</head>
<body>
<main class="canvas">
  <section class="card card--front">
    <div class="brand">
      <span class="brand__dot"></span>
      <span class="brand__name">
        <span class="brand__main">Talvex</span>
        <span class="brand__sub">Industrial Maintenance</span>
      </span>
    </div>
    <div class="contact">
      <p class="contact__name">Dale Virnow Jr.</p>
      <div class="contact__rule"></div>
      <p class="contact__line">413-627-8154</p>
      <p class="contact__line">dale.virnow.jr@brindlemail.net</p>
    </div>
  </section>

  <section class="card card--back">
    <div class="back-texture" role="img" aria-label="Embossed repeating brand pattern on blue"></div>
    <div class="brand brand--reverse">
      <span class="brand__dot"></span>
      <span class="brand__name">
        <span class="brand__main">Talvex</span>
        <span class="brand__sub">Industrial Maintenance</span>
      </span>
    </div>
  </section>
</main>
</body>
</html>
```